Ghost Tour and Pub Crawl Rack Card Brochure

We are looking to get an updated design for our rack cards that are printed on 4x9 vertical cards. We have uploaded our logo and our previous design. We are looking for a new idea. We need something that jumps out at you when they are printed and sitting next to a group of 50 other brochures. It needs to have all of the must haves incorporated.

Target Market(s)

Women

Industry/Entity Type

Tourism

Font styles to use
Serif
Sans Serif
Decorative
Script
Other font styles liked:
• Doesn't Matter

Colors

Designer to choose colors to be used in the design.

Requirements
Must have
• Needs to be a design that jumps out at you when you are looking at 50 of these in a rack from all different companies.
• 1. Instead of it being just Ghost Tour Pub Crawl, we would like it to have some sort of design that is Ghost Tours and Pub Crawls.
• 2. Our Website must be prominent www.DuskWanderers.com
• 2. We want a box for text at the bottom that we can add a promo code ourselves to the design, so just something that we can edit later that allows us to have enough space to write a promo code, city name, and alternate phone number.
• 3. We want it to say save 10% instead of $5.00
• 4. Phone number 1-8-Lamp-Walk listed on the card
Nice to have
• Needs to be Spooky, but stand out.

```html
<!DOCTYPE html>
<html lang="en">
<head>
<meta charset="utf-8">
<title>Dusk Wanderers Rack Card</title>
<link rel="stylesheet" href="https://fonts.googleapis.com/css2?family=Bebas+Neue&family=Kaushan+Script&family=Oswald:wght@300;500&family=Rye&family=Yellowtail&display=block">
<style>
  :root {
    --page: #2b3a22;
    --night: #05080b;
    --forest: #0e2330;
    --moon: #1f6f8f;
    --white: #ffffff;
    --orange: #f7931e;
    --neon-cyan: #5fe0ff;
    --neon-pink: #ff6fb5;
  }
  * { margin: 0; padding: 0; box-sizing: border-box; }
  html, body { width: 960px; height: 1200px; overflow: hidden; background: var(--page); }
  .rack-card {
    position: absolute; left: 213px; top: 0;
    width: 534px; height: 1200px; overflow: hidden;
    background: var(--night);
    color: var(--white);
  }
  .forest-scene {
    position: absolute; inset: 0;
    background:
      radial-gradient(circle at 50% 53%, var(--moon) 0, #14475c 90px, transparent 190px),
      linear-gradient(180deg, #0b1820 0%, var(--forest) 40%, #0a1a22 62%, var(--night) 80%);
  }
  .brand-name {
    position: absolute; top: 160px; left: 0; width: 100%;
    text-align: center; font-family: "Rye", serif;
    font-size: 44px; color: var(--white);
  }
  .title-ghost, .title-tour {
    position: absolute; font-family: "Rye", serif; color: var(--white); line-height: 1;
  }
  .title-ghost { left: 36px; top: 277px; font-size: 62px; }
  .title-tour { left: 266px; top: 344px; font-size: 70px; }
  .mug-art {
    position: absolute; left: 22px; top: 420px; width: 110px; height: 106px;
    background: radial-gradient(ellipse at 50% 50%, rgba(120,140,150,.28) 0, rgba(120,140,150,.1) 45%, transparent 70%);
  }
  .title-pub, .title-crawl {
    position: absolute; font-family: "Yellowtail", "Kaushan Script", cursive;
    color: var(--orange); line-height: 1; white-space: nowrap;
  }
  .title-pub { left: 150px; top: 418px; font-size: 138px; }
  .title-crawl { left: 212px; top: 540px; font-size: 124px; }
  .offer-save, .offer-percent {
    position: absolute; font-family: "Bebas Neue", sans-serif; line-height: 1;
    color: transparent;
  }
  .offer-save {
    left: 40px; top: 705px; font-size: 118px;
    -webkit-text-stroke: 3px var(--neon-cyan);
    text-shadow: 0 0 10px rgba(95,224,255,.7);
  }
  .offer-percent {
    left: 240px; top: 690px; font-size: 165px;
    -webkit-text-stroke: 3px var(--neon-pink);
    text-shadow: 0 0 12px rgba(255,111,181,.7);
  }
  .offer-percent .sign { font-size: 92px; vertical-align: top; position: relative; top: 12px; }
  .offer-unit {
    position: absolute; left: 48px; top: 814px;
    font-family: "Rye", serif; font-size: 26px; color: var(--orange);
  }
  .website, .phone {
    position: absolute; left: 0; width: 100%; text-align: center;
    font-family: "Oswald", sans-serif; line-height: 1.2;
  }
  .website { top: 880px; font-size: 38px; font-weight: 500; }
  .phone { top: 940px; font-size: 42px; font-weight: 300; }
  .promo-box {
    position: absolute; left: 119px; top: 1017px; width: 294px; height: 126px;
    border: 1.5px solid var(--white);
    display: flex; flex-direction: column; justify-content: space-around; align-items: center;
    padding: 8px 0;
    font-family: Arial, Helvetica, sans-serif; font-size: 19px;
  }
</style>
</head>
<body>
  <main class="rack-card">
    <div class="forest-scene" role="img" aria-label="Dark misty forest of bare trees under a glowing blue full moon"></div>
    <div class="brand-name">Dusk Wanderers</div>
    <div class="title-ghost">GHOST</div>
    <div class="title-tour">TOUR</div>
    <div class="mug-art" role="img" aria-label="Line drawing of a tipped beer mug spilling foam"></div>
    <div class="title-pub">Pub</div>
    <div class="title-crawl">Crawl</div>
    <div class="offer-save">SAVE</div>
    <div class="offer-percent">10<span class="sign">%</span></div>
    <div class="offer-unit">per ticket</div>
    <div class="website">www.DuskWanderers.com</div>
    <div class="phone">call-1-8-Lamp-Walk</div>
    <div class="promo-box">
      <span>Add your promo code</span>
      <span>City Name</span>
      <span>Phone number</span>
    </div>
  </main>
</body>
</html>
```